Pack design: Meal Kits for older consumers - VITACRUM

Pack design for a new to market Meal Kit specifically designed for the older consumer (over 65)

VITACRUM - tiny plates of goodness for GRAND PLATES OF TIME
fortified and nutritious small portion meals for older consumers.

Target Market(s)

Over 65 year olds

Industry/Entity Type

Food Production

Font styles to use
Sans Serif

Colors
6b449b
b768aa
b7a5cd
ffffff
e4daeb
ecdaeb

Requirements
Must have
• Pack design that is appealing to the 0ver 65s but MUST not be patronising.
• Large easy to read font
Nice to have
• Logo
• Instructions inside pack

```html
<!DOCTYPE html>
<html lang="en">
<head>
<meta charset="utf-8">
<title>VITACRUM – Meal Kit Sleeve</title>
<link rel="stylesheet" href="https://fonts.googleapis.com/css2?family=Oswald:wght@400;500;600&family=Roboto+Condensed:wght@700&display=swap">
<style>
  :root {
    --purple-deep: #6b449b;
    --purple-mid: #b768aa;
    --lilac: #b7a5cd;
    --white: #ffffff;
    --mist: #e4daeb;
    --blush: #ecdaeb;
    --stage: #e7e7e9;
    --photo-dark: #3b3a36;
    --photo-warm: #8a7a62;
  }
  * { box-sizing: border-box; margin: 0; padding: 0; }
  html, body { width: 1200px; height: 837px; overflow: hidden; }
  body {
    background: var(--stage);
    font-family: "Oswald", sans-serif;
    color: var(--purple-deep);
  }
  .sleeve {
    position: absolute;
    left: 280px; top: 18px;
    width: 640px; height: 800px;
    background: var(--white);
    box-shadow: 0 6px 24px rgba(0,0,0,.12);
  }
  .sleeve__edge {
    position: absolute; top: 0; bottom: 0; width: 34px;
    background: linear-gradient(180deg, var(--purple-mid), var(--purple-deep) 50%, var(--purple-mid));
  }
  .sleeve__edge--left { left: 0; }
  .sleeve__edge--right { right: 0; }

  .brand {
    position: absolute; top: 62px; left: 0; right: 0;
    display: flex; justify-content: center; align-items: center; gap: 14px;
  }
  .brand__dot {
    width: 26px; height: 26px; border-radius: 50%;
    border: 3px solid var(--purple-deep);
  }
  .brand__name {
    font-family: "Oswald", sans-serif;
    font-weight: 500; font-size: 50px; letter-spacing: 2px;
    color: var(--purple-deep);
  }
  .tagline { position: absolute; top: 140px; left: 50px; width: 540px; height: 110px; }

  .product {
    position: absolute; top: 300px; left: 60px; width: 230px;
    text-align: center;
    font-weight: 500; font-size: 36px; line-height: 56px;
    color: var(--purple-deep);
  }
  .product-photo {
    position: absolute; top: 296px; left: 326px; width: 270px; height: 180px;
  }
  .product-photo__frame {
    position: absolute; left: -8px; top: 8px; width: 262px; height: 180px;
    background: var(--lilac);
  }
  .product-photo__image {
    position: absolute; inset: 0;
    background: radial-gradient(circle at 45% 55%, #6d8a4a 0 18%, var(--photo-dark) 42%, var(--photo-warm) 100%);
  }

  .benefits {
    position: absolute; top: 638px; left: 40px; right: 40px;
    display: flex; justify-content: space-around; align-items: center;
  }
  .benefit {
    width: 90px; height: 90px; border-radius: 50%;
    background: var(--purple-deep); color: var(--white);
    display: flex; flex-direction: column; align-items: center; justify-content: center;
    font-family: "Roboto Condensed", sans-serif; font-weight: 700;
    text-align: center; line-height: 1;
  }
  .benefit__big { font-size: 20px; }
  .benefit__small { font-size: 13px; }
  .benefit__tiny { font-size: 9px; font-weight: 400; letter-spacing: .3px; }
</style>
</head>
<body>
  <main class="sleeve">
    <div class="sleeve__edge sleeve__edge--left" role="img" aria-label="Purple and pink checked border pattern"></div>
    <div class="sleeve__edge sleeve__edge--right" role="img" aria-label="Purple and pink checked border pattern"></div>

    <header class="brand">
      <span class="brand__dot"></span>
      <span class="brand__name">VITACRUM</span>
    </header>

    <svg class="tagline" viewBox="0 0 540 110" aria-label="Tiny plates of goodness for grand plates of time">
      <path d="M0 40 L40 48 L30 62 L44 76 L6 70 Z" fill="#6b449b"/>
      <path d="M540 40 L500 48 L510 62 L496 76 L534 70 Z" fill="#6b449b"/>
      <path d="M30 36 Q270 -4 510 36 L510 80 Q270 40 30 80 Z" fill="#6b449b"/>
      <path id="ribbon-line" d="M40 66 Q270 26 500 66" fill="none"/>
      <text font-family="Roboto Condensed, sans-serif" font-weight="700" font-size="17" fill="#ffffff" letter-spacing=".5">
        <textPath href="#ribbon-line" startOffset="50%" text-anchor="middle">TINY PLATES OF GOODNESS FOR GRAND PLATES OF TIME</textPath>
      </text>
    </svg>

    <h1 class="product">Japanese Ramen Broths with fresh vegetables</h1>

    <figure class="product-photo">
      <div class="product-photo__frame"></div>
      <div class="product-photo__image" role="img" aria-label="Photo of a bowl of ramen broth with egg, greens, mushrooms and chopsticks"></div>
    </figure>

    <ul class="benefits">
      <li class="benefit"><span class="benefit__small">SMALL</span><span class="benefit__small">but mighty</span><span class="benefit__tiny">portions</span></li>
      <li class="benefit">
        <svg width="34" height="34" viewBox="0 0 34 34" fill="none" stroke="#fff" stroke-width="3" aria-hidden="true">
          <path d="M17 4 L24 15 M24 15 L18 15 M24 15 L26 9"/><path d="M30 26 L18 30 M18 30 L22 25 M18 30 L23 33"/><path d="M4 26 L10 14 M10 14 L12 20 M10 14 L5 17"/>
        </svg>
        <span class="benefit__tiny">all recyclable</span>
      </li>
      <li class="benefit"><span class="benefit__big">EASY</span><span class="benefit__small">TO USE</span></li>
      <li class="benefit">
        <svg width="26" height="30" viewBox="0 0 26 30" fill="none" stroke="#fff" stroke-width="2.5" aria-hidden="true">
          <path d="M2 6 H24 M9 6 V2 H17 V6 M5 6 L7 28 H19 L21 6 M11 11 V23 M15 11 V23"/>
        </svg>
        <span class="benefit__small">no waste</span>
      </li>
      <li class="benefit"><span class="benefit__small">PROTEIN</span><span class="benefit__big">+</span><span class="benefit__small">Calcium</span></li>
    </ul>
  </main>
</body>
</html>
```